Stationary and business cards for Meridale Wellness Clinic
Brightwater Meridale Wellness Clinic
Stationary and business cards for Meridale Wellness Clinic - Health
Creative Brief
Use same font as used in my logo
Use whatever fonts you feel works with the logo
Bright & Fun-filled
Dr. Marcus T. Falk
Chiropractic Physician
5182 Orvalle Park Rd. Ste. B Sarasota, FL 34871
wellpath7crew@mailnest.example
www.falkspinecare.example
when they go to the website, they need to click on other services in the top right of the page, and go to: functional endocrine, to read about what I do . I'm not sure how we can direct them to do that on a business card. Also, this is a separate business located within Falk Chiropractic Center,and has nothing to do with Chiropractic Care...... Use whatever fonts you feel works with the logo, or the same as the logo
Lack of energy, sleep problems, weight gain, and body pains are not normal processes of aging...You don't have to live with it! Call us today to reserve a seat at our next free seminar to learn how we can help you!

```html
<!DOCTYPE html>
<html lang="en">
<head>
<meta charset="utf-8">
<title>Meridale Wellness Clinic – Business Cards</title>
<link href="https://fonts.googleapis.com/css2?family=Open+Sans:wght@400;600;700&family=Noto+Serif:wght@400;700&display=swap" rel="stylesheet">
<style>
  :root{
    --bg:#e9eaea;
    --card:#ffffff;
    --green:#5a9e1e;
    --green-dark:#3f8a16;
    --orange:#ef6a1c;
    --text:#555555;
    --rule:#cfcfcf;
  }
  *{box-sizing:border-box;margin:0;padding:0}
  html,body{width:1200px;height:852px;overflow:hidden;background:var(--bg)}
  .canvas{position:relative;width:1200px;height:852px}
  .card{position:absolute;width:560px;height:320px;background:var(--card);border-radius:16px;overflow:hidden;box-shadow:0 4px 14px rgba(0,0,0,.18);font-family:"Open Sans",sans-serif;color:var(--text)}
  .card--front{left:90px;top:90px}
  .card--alt{left:550px;top:440px}
  .swoosh{position:absolute;left:0;bottom:0;width:560px;height:110px}
  .brand{position:absolute;display:flex;align-items:center;gap:10px}
  .brand__dot{width:44px;height:44px;border-radius:50%;background:var(--green);flex:none}
  .brand__name{font-family:"Open Sans",sans-serif;font-weight:700;color:var(--green);line-height:1.05;font-size:25px;letter-spacing:.5px;white-space:nowrap}
  .brand__name small{display:block;font-size:13px;letter-spacing:1.2px;font-weight:700}
  .person__name{font-family:"Noto Serif",serif;font-weight:700;color:var(--green-dark);font-size:16px}
  .person__title{font-family:"Noto Serif",serif;font-weight:700;color:var(--orange);font-size:12.5px;margin-top:4px}
  .person__addr{font-family:"Noto Serif",serif;font-size:11.5px;line-height:1.5;margin-top:8px}
  .contacts{list-style:none;font-size:11.5px;line-height:1}
  .contacts li{display:flex;align-items:center;gap:8px;margin-bottom:7px;white-space:nowrap}
  .icon{width:13px;height:13px;flex:none}
  .divider{position:absolute;width:1px;background:var(--rule)}
  .card--front .brand{left:36px;top:44px}
  .card--front .person{position:absolute;left:36px;top:130px;text-align:right;width:220px}
  .card--front .divider{left:270px;top:128px;height:100px}
  .card--front .contacts{position:absolute;left:288px;top:132px}
  .card--alt .brand{left:26px;top:172px;gap:8px}
  .card--alt .brand__dot{width:36px;height:36px}
  .card--alt .brand__name{font-size:20px;letter-spacing:.3px}
  .card--alt .brand__name small{font-size:10px;letter-spacing:.8px}
  .card--alt .divider{left:278px;top:34px;height:180px}
  .card--alt .person{position:absolute;left:294px;top:36px}
  .card--alt .contacts{position:absolute;left:294px;top:132px}
</style>
</head>
<body>
<main class="canvas">

  <article class="card card--front">
    <div class="brand">
      <span class="brand__dot"></span>
      <p class="brand__name">BRIGHTWATER<small>MERIDALE WELLNESS CLINIC</small></p>
    </div>
    <div class="person">
      <p class="person__name">Dr. Marcus T. Falk</p>
      <p class="person__title">Chiropractic Physician</p>
      <p class="person__addr">5182 Orvalle Park Rd. Ste. B<br>Sarasota, FL 34871</p>
    </div>
    <span class="divider"></span>
    <ul class="contacts">
      <li><svg class="icon" viewBox="0 0 16 16"><path fill="#5a9e1e" d="M4 1l3 3-2 2c1 2 3 4 5 5l2-2 3 3-2 2C7 14 2 9 2 3z"/></svg>941.555.0137</li>
      <li><svg class="icon" viewBox="0 0 16 16"><rect x="3" y="2" width="10" height="5" fill="#5a9e1e"/><rect x="1" y="7" width="14" height="6" rx="1" fill="#5a9e1e"/></svg>941.555.0138</li>
      <li><svg class="icon" viewBox="0 0 16 16"><rect x="1" y="3" width="14" height="10" rx="1" fill="#5a9e1e"/><path d="M1 4l7 5 7-5" stroke="#fff" fill="none"/></svg>wellpath7crew@mailnest.example</li>
      <li><svg class="icon" viewBox="0 0 16 16"><circle cx="8" cy="8" r="7" fill="#5a9e1e"/><path d="M1 8h14M8 1c-3 4-3 10 0 14M8 1c3 4 3 10 0 14" stroke="#fff" fill="none"/></svg>www.falkspinecare.example</li>
    </ul>
    <svg class="swoosh" viewBox="0 0 560 110" preserveAspectRatio="none">
      <path d="M0 20 C180 50 380 60 560 40 L560 110 L0 110Z" fill="var(--orange)"/>
      <path d="M0 30 C180 62 380 72 560 54 L560 110 L0 110Z" fill="#fff"/>
      <path d="M0 40 C180 74 380 84 560 66 L560 110 L0 110Z" fill="var(--green)"/>
    </svg>
  </article>

  <article class="card card--alt">
    <div class="brand">
      <span class="brand__dot"></span>
      <p class="brand__name">BRIGHTWATER<small>MERIDALE WELLNESS CLINIC</small></p>
    </div>
    <span class="divider"></span>
    <div class="person">
      <p class="person__name">Dr. Marcus T. Falk</p>
      <p class="person__title">Chiropractic Physician</p>
      <p class="person__addr">5182 Orvalle Park Rd. Ste. B<br>Sarasota, FL 34871</p>
    </div>
    <ul class="contacts">
      <li><svg class="icon" viewBox="0 0 16 16"><path fill="#5a9e1e" d="M4 1l3 3-2 2c1 2 3 4 5 5l2-2 3 3-2 2C7 14 2 9 2 3z"/></svg>941.555.0137</li>
      <li><svg class="icon" viewBox="0 0 16 16"><rect x="3" y="2" width="10" height="5" fill="#5a9e1e"/><rect x="1" y="7" width="14" height="6" rx="1" fill="#5a9e1e"/></svg>941.555.0138</li>
      <li><svg class="icon" viewBox="0 0 16 16"><rect x="1" y="3" width="14" height="10" rx="1" fill="#5a9e1e"/><path d="M1 4l7 5 7-5" stroke="#fff" fill="none"/></svg>wellpath7crew@mailnest.example</li>
      <li><svg class="icon" viewBox="0 0 16 16"><circle cx="8" cy="8" r="7" fill="#5a9e1e"/><path d="M1 8h14M8 1c-3 4-3 10 0 14M8 1c3 4 3 10 0 14" stroke="#fff" fill="none"/></svg>www.falkspinecare.example</li>
    </ul>
    <svg class="swoosh" viewBox="0 0 560 110" preserveAspectRatio="none">
      <path d="M0 58 C180 88 380 82 560 30 L560 110 L0 110Z" fill="var(--orange)"/>
      <path d="M0 66 C180 98 380 92 560 42 L560 110 L0 110Z" fill="#fff"/>
      <path d="M0 74 C180 106 380 102 560 54 L560 110 L0 110Z" fill="var(--green)"/>
    </svg>
  </article>

</main>
</body>
</html>
```